Website Design

Looking for a less than 30 page website for a new tree service company. Most of the pages would be copies of one another but for each geographical area we service. So, for five areas, we would replicate six services for each area.

Coding

Coded - Design and coding required

```html
<!DOCTYPE html>
<html lang="en">
<head>
<meta charset="utf-8">
<title>Oakline Tree Services</title>
<link href="https://fonts.googleapis.com/css2?family=Rubik:wght@500;600;700&family=Be+Vietnam+Pro:wght@400;500;600&display=swap" rel="stylesheet">
<style>
:root{
  --forest:#233612;
  --forest-deep:#1b2a0d;
  --leaf:#1f9d3a;
  --amber:#f7a900;
  --ink:#1d1d1d;
  --muted:#6b6b6b;
  --paper:#f5f5f5;
  --white:#ffffff;
  --night:#1a1a1a;
}
*{margin:0;padding:0;box-sizing:border-box}
html,body{width:1200px;height:4456px;overflow:hidden}
body{position:relative;font-family:"Be Vietnam Pro",sans-serif;color:var(--ink);background:var(--white)}
.abs{position:absolute}
h1,h2,h3,h4{font-family:"Rubik",sans-serif}
.eyebrow{font-size:12px;letter-spacing:2px;text-transform:uppercase;color:var(--amber);font-weight:500}
.btn{display:flex;align-items:center;justify-content:center;gap:10px;background:var(--amber);color:var(--forest-deep);font-family:"Rubik",sans-serif;font-weight:500;font-size:15px;border-radius:0 14px 14px 14px}
.dot{width:14px;height:14px;border-radius:50%;background:currentColor;display:inline-block}

/* top bar */
.topbar{left:0;top:0;width:1200px;height:42px;background:var(--forest-deep);color:var(--white);font-size:12px}
.topbar .socials{left:76px;top:14px;display:flex;gap:12px}
.topbar .contact{right:70px;top:14px;display:flex;gap:20px}
.topbar .contact span::before{content:"";display:inline-block;width:7px;height:7px;background:var(--leaf);border-radius:2px;margin-right:7px}

/* header */
.header{left:0;top:42px;width:1200px;height:91px;background:var(--white)}
.nav{top:38px;display:flex;gap:36px;font-family:"Rubik",sans-serif;font-size:13px;font-weight:500;color:var(--forest-deep)}
.nav.left{left:132px}
.nav.right{left:679px}
.brand{left:494px;top:42px;width:137px;height:126px;background:var(--white);display:flex;flex-direction:column;align-items:center;justify-content:center;gap:8px;z-index:3}
.brand .mark{width:22px;height:22px;border-radius:50%;background:var(--amber)}
.brand .name{font-family:"Rubik",sans-serif;font-weight:700;font-size:20px;color:var(--forest)}
.quote-btn{left:904px;top:67px;width:164px;height:42px;font-size:14px}

/* hero */
.hero{left:0;top:133px;width:1200px;height:593px;background:linear-gradient(100deg,#1f5a1a 0%,#2f7a24 45%,#4b8f35 70%,#2d5f20 100%)}
.hero .eyebrow{left:81px;top:166px}
.hero h1{left:81px;top:196px;font-size:62px;font-weight:700;color:var(--white);letter-spacing:.5px}
.hero p{left:81px;top:286px;width:620px;font-size:13px;line-height:28px;color:var(--white)}
.hero .btn{left:81px;top:373px;width:178px;height:52px;font-size:15px}
.hero .side-social{left:1074px;top:210px;display:flex;flex-direction:column;gap:38px;color:var(--white)}
.hero .side-social .dot{width:12px;height:12px}

.features{left:66px;top:650px;width:1068px;height:140px;background:var(--forest);border-radius:6px;display:flex;padding:28px 0 0 28px;gap:0}
.feature{width:346px;display:flex;align-items:center;gap:16px;color:var(--white);font-family:"Rubik",sans-serif;font-weight:600;font-size:19px;line-height:26px}
.feature .icon{width:76px;height:80px;background:var(--white);border-radius:8px;display:flex;align-items:center;justify-content:center;flex:none}

/* about */
.about{left:0;top:790px;width:1200px;height:619px;background:var(--paper)}
.about .photo-main{left:74px;top:85px;width:472px;height:387px;border-radius:18px 0 18px 18px;background:linear-gradient(160deg,#6b8f2a,#3f6b1f 60%,#8aa24a)}
.about .photo-round{left:349px;top:296px;width:242px;height:242px;border-radius:50%;border:8px solid var(--white);background:radial-gradient(circle at 50% 45%,#7a6a2a,#3d5a1c 70%)}
.about .eyebrow{left:631px;top:104px}
.about h2{left:631px;top:138px;font-size:44px;line-height:48px;font-weight:700;color:var(--forest)}
.about p{left:631px;top:300px;width:470px;font-size:13px;line-height:29px;color:#555}
.about .btn{left:631px;top:474px;width:159px;height:40px;font-size:14px}

/* services */
.services{left:0;top:1409px;width:1200px;height:550px;background:linear-gradient(180deg,#2f6e23 0%,#4f8f31 40%,#3f8a2a 70%,#2e7a20 100%)}
.services .eyebrow{left:0;width:1200px;text-align:center;top:166px}
.services h2{left:0;width:1200px;text-align:center;top:195px;font-size:44px;font-weight:700;color:var(--white)}
.services p{left:0;width:1200px;text-align:center;top:270px;font-size:13px;color:var(--white)}
.service-card{top:1743px;width:327px;height:266px;background:var(--white);border-radius:4px;box-shadow:0 8px 24px rgba(0,0,0,.08);text-align:center;padding-top:30px}
.service-card h3{color:var(--leaf);font-size:19px;font-weight:600;margin-top:18px}
.service-card p{color:#666;font-size:13px;line-height:29px;margin-top:14px}
.service-card .more{display:inline-block;margin-top:18px;color:var(--leaf);font-size:13px;padding-bottom:8px;border-bottom:1px solid var(--leaf)}

/* why */
.why .eyebrow{left:81px;top:2126px}
.why h2{left:81px;top:2152px;font-size:44px;line-height:47px;font-weight:700;color:var(--forest)}
.why p.lead{left:81px;top:2272px;width:450px;font-size:13px;line-height:29px;color:#555}
.why .photo{left:81px;top:2358px;width:450px;height:187px;border-radius:16px;background:linear-gradient(110deg,#4c7a24,#7fa84a 55%,#5f8f3a)}
.why-card{width:259px;background:var(--white);box-shadow:0 8px 22px rgba(0,0,0,.08);border-radius:4px;padding:28px 30px}
.why-card h4{font-size:20px;font-weight:600;color:var(--forest)}
.why-card p{font-size:13px;line-height:29px;color:#666;margin-top:16px}
.why-card.dark{background:var(--forest)}
.why-card.dark h4,.why-card.dark p{color:var(--white)}

/* blog */
.blog .eyebrow{left:0;width:1200px;text-align:center;top:2658px}
.blog h2{left:0;width:1200px;text-align:center;top:2684px;font-size:44px;font-weight:700;color:var(--leaf)}
.post{top:2756px;width:336px;height:405px;background:var(--paper);border-radius:0 0 16px 16px;overflow:hidden}
.post .thumb{height:221px;position:relative}
.post .tag{position:absolute;right:0;top:0;background:var(--amber);color:var(--white);font-size:10px;padding:5px 12px;text-transform:uppercase}
.post h3{font-size:17px;line-height:24px;font-weight:600;color:var(--forest);margin:24px 19px 0}
.post p{font-size:11px;line-height:19px;color:#777;margin:16px 19px 0}

/* hire */
.hire{left:0;top:3252px;width:1200px;height:669px;background:linear-gradient(100deg,#1f4a18 0%,#2f6a22 45%,#4f7a2a 65%,#234e1a 100%)}
.hire .eyebrow{left:95px;top:152px;color:var(--white)}
.hire h2{left:95px;top:178px;width:560px;font-size:43px;line-height:46px;font-weight:700;color:var(--white)}
.hire p{left:95px;top:392px;width:530px;font-size:13px;line-height:29px;color:var(--white)}
.hire .btn{left:95px;top:477px;width:130px;height:42px;font-size:14px}
.hire .play{left:886px;top:302px;width:68px;height:68px;border-radius:50%;background:var(--amber);border:6px solid rgba(255,255,255,.35);display:flex;align-items:center;justify-content:center}

/* footer */
.footer{left:0;top:3921px;width:1200px;height:535px;background:var(--night);color:var(--white)}
.footer-card{left:74px;top:3871px;width:420px;height:434px;background:var(--white);border-radius:6px}
.footer-card .brandline{position:absolute;left:46px;top:70px;display:flex;align-items:center;gap:12px;font-family:"Rubik",sans-serif;font-weight:700;font-size:34px;color:var(--forest)}
.footer-card .brandline .mark{width:30px;height:30px;background:var(--amber);border-radius:50%}
.footer-card p{position:absolute;left:46px;top:245px;width:340px;font-size:13px;line-height:29px;color:#555}
.footer-card .socials{position:absolute;left:54px;top:365px;display:flex;gap:16px;color:var(--leaf)}
.footer-card .socials .dot{width:12px;height:12px}
.fcol{top:4006px}
.fcol h4{font-size:17px;font-weight:600;margin-bottom:22px}
.fcol li{list-style:none;font-size:13px;margin-bottom:14px}
.office-item{display:flex;gap:12px;margin-bottom:20px;font-size:12px;line-height:19px}
.office-item i{width:13px;height:13px;background:var(--amber);border-radius:2px;flex:none;margin-top:3px}
.office-item b{font-weight:600;display:block}
.footer .rule{left:74px;top:431px;width:1052px;height:1px;background:#2f6a22}
.footer .copy{left:84px;top:450px;font-size:12px}
.footer .legal{right:84px;top:450px;font-size:12px;display:flex;gap:20px}
.footer .legal span::before{content:"";display:inline-block;width:9px;height:9px;border-radius:50%;background:var(--amber);margin-right:6px}
</style>
</head>
<body>

<div class="abs topbar">
  <div class="abs socials"><span class="dot" style="width:11px;height:11px"></span><span class="dot" style="width:11px;height:11px"></span><span class="dot" style="width:11px;height:11px"></span></div>
  <div class="abs contact"><span>+1 555 014 8220</span><span>hello@oakline.example</span></div>
</div>

<header class="abs header">
  <nav class="abs nav left"><span>HOME</span><span>ABOUT</span><span>SERVICES</span><span>GALLERY</span></nav>
  <nav class="abs nav right"><span>BLOG</span><span>FAQS</span><span>CONTACT</span></nav>
</header>
<div class="abs brand"><span class="mark"></span><span class="name">Oakline</span></div>
<div class="abs btn quote-btn">Get a Free Quote</div>

<section class="abs hero" role="img" aria-label="Gloved hand pruning a green conifer hedge with secateurs">
  <div class="abs eyebrow">Welcome</div>
  <h1 class="abs">OAKLINE TREE SERVICES</h1>
  <p class="abs">Lorem ipsum dolor sit amet, consectetur adipiscing elit. Ut elit tellus, luctus nec ullamcorper mattis, pulvinar dapibus leo.</p>
  <div class="abs btn">Discover More</div>
  <div class="abs side-social"><span class="dot"></span><span class="dot"></span><span class="dot"></span><span class="dot"></span></div>
</section>

<div class="abs features">
  <div class="feature"><span class="icon"><svg width="40" height="40" viewBox="0 0 40 40" fill="none" stroke="#f7a900" stroke-width="2"><circle cx="20" cy="14" r="7"/><path d="M9 36c0-7 5-12 11-12s11 5 11 12"/><path d="M12 12h16"/></svg></span>Skilled Gardener &amp;<br>Technician</div>
  <div class="feature"><span class="icon"><svg width="40" height="40" viewBox="0 0 40 40" fill="none" stroke="#f7a900" stroke-width="2"><circle cx="20" cy="14" r="7"/><path d="M9 36c0-7 5-12 11-12s11 5 11 12"/><path d="M11 14a9 9 0 0 1 18 0"/></svg></span>Awesome Customer<br>Service</div>
  <div class="feature"><span class="icon"><svg width="40" height="40" viewBox="0 0 40 40" fill="none" stroke="#f7a900" stroke-width="2"><path d="M20 4l13 5v10c0 9-6 15-13 17C13 34 7 28 7 19V9z"/><path d="M14 20l4 4 8-8"/></svg></span>Guarantee Service</div>
</div>

<section class="abs about">
  <div class="abs photo-main" role="img" aria-label="Gardener trimming round shrubs beside a lawn"></div>
  <div class="abs photo-round" role="img" aria-label="Worker clearing autumn leaves in a park"></div>
  <div class="abs eyebrow">About Us</div>
  <h2 class="abs">We Are Professional<br>Tree Care Services<br>Company</h2>
  <p class="abs">Condimentum mauris pede dolor cras enim nibh sollicitudin purus hendrerit libero. Quis placerat torquent montes aliquam consequat proin massa adipiscing pharetra. A nibh semper himenaeos faucibus curabitur efficitur pretium at fames cubilia bibendum. Nec eleifend aliquet velit vitae semper.</p>
  <div class="abs btn">Learn More <span>&rarr;</span></div>
</section>

<section class="abs services" role="img" aria-label="Soft-focus green lawn with hedges">
  <div class="abs eyebrow">What We Do</div>
  <h2 class="abs">Professional Service</h2>
  <p class="abs">Lorem ipsum dolor sit amet, consectetur adipiscing elit. Ut elit tellus, luctus nec ullamcorper mattis, pulvinar dapibus leo.</p>
</section>
<div class="abs service-card" style="left:90px"><svg width="40" height="40" viewBox="0 0 40 40" fill="none" stroke="#1f9d3a" stroke-width="2"><path d="M8 34l20-20 4-8-8 4L4 30z"/><path d="M14 24l4 4M18 20l4 4"/></svg><h3>TREE REMOVAL</h3><p>Sociosqu ipsum convallis conubia<br>vivamus nec ornare eget</p><span class="more">Learn more &rarr;</span></div>
<div class="abs service-card" style="left:436px"><svg width="40" height="40" viewBox="0 0 40 40" fill="none" stroke="#1f9d3a" stroke-width="2"><circle cx="11" cy="29" r="5"/><path d="M15 25L32 8M24 8h8v8"/></svg><h3>TREE CARE</h3><p>Sociosqu ipsum convallis conubia<br>vivamus nec ornare eget</p><span class="more">Learn more &rarr;</span></div>
<div class="abs service-card" style="left:782px"><svg width="40" height="40" viewBox="0 0 40 40" fill="none" stroke="#1f9d3a" stroke-width="2"><path d="M20 4l7 10h-4l7 10h-5l6 9H9l6-9h-5l7-10h-4z"/><path d="M20 33v5"/></svg><h3>STORM DAMAGE</h3><p>Sociosqu ipsum convallis conubia<br>vivamus nec ornare eget</p><span class="more">Learn more &rarr;</span></div>

<section class="why">
  <div class="abs eyebrow">Why Choose Us</div>
  <h2 class="abs">Affordable Price and<br>Reasonable Service.</h2>
  <p class="abs lead">Lorem ipsum dolor sit amet, consectetur adipiscing elit. Ut elit tellus, luctus nec ullamcorper mattis, pulvinar dapibus leo.</p>
  <div class="abs photo" role="img" aria-label="Gloved hand cutting a hedge with pruning shears"></div>
  <div class="abs why-card" style="left:572px;top:2140px;height:189px"><h4>Experienced</h4><p>Commodo porttitor taciti lacinia elit nibh molestie metus tincidunt pellentesque.</p></div>
  <div class="abs why-card" style="left:851px;top:2140px;height:189px"><h4>Expertise</h4><p>Commodo porttitor taciti lacinia elit nibh molestie metus tincidunt pellentesque.</p></div>
  <div class="abs why-card" style="left:572px;top:2348px;height:197px"><h4>Dedicated</h4><p>Commodo porttitor taciti lacinia elit nibh molestie metus tincidunt pellentesque.</p></div>
  <div class="abs why-card dark" style="left:851px;top:2348px;height:197px"><h4>24/7 Support</h4><p>Commodo porttitor taciti lacinia elit nibh molestie metus tincidunt pellentesque.</p></div>
</section>

<section class="blog">
  <div class="abs eyebrow">Update</div>
  <h2 class="abs">Latest News &amp; Blog</h2>
  <article class="abs post" style="left:81px"><div class="thumb" role="img" aria-label="Family in a garden beside a wooden shed" style="background:linear-gradient(150deg,#5a6b2a,#8a7a3a 50%,#4f7a2a)"><span class="tag">Uncategorized</span></div><h3>Everything You Need To Know About Lawn Maintenance Drought</h3><p>Lorem ipsum dolor sit amet, consectetuer adipiscing elit. Aenean commodo ligula eget dolor. Aenean massa. Cum sociis natoque penatibus et magnis dis parturient montes, nascetur</p></article>
  <article class="abs post" style="left:432px"><div class="thumb" role="img" aria-label="House surrounded by tall shade trees" style="background:linear-gradient(160deg,#6f8f4a,#3f6a2a 60%,#5a7a3a)"><span class="tag">Uncategorized</span></div><h3>Benefits Of Tree Coverage: Is Your Home Made In The Shade?</h3><p>Lorem ipsum dolor sit amet, consectetuer adipiscing elit. Aenean commodo ligula eget dolor. Aenean massa. Cum sociis natoque penatibus et magnis dis parturient montes, nascetur</p></article>
  <article class="abs post" style="left:783px"><div class="thumb" role="img" aria-label="Gardener pushing a lawn mower" style="background:linear-gradient(160deg,#3f6a22,#6a8a3a 50%,#c86a2a)"><span class="tag">Uncategorized</span></div><h3>Ask The Agronomists: Lawncare Tips From The Experts</h3><p>Welcome to our journal. This is our first post. Read on for simple seasonal lawn care advice!</p></article>
</section>

<section class="abs hire" role="img" aria-label="Worker with leaf blower among park trees">
  <div class="abs eyebrow">Hire Us</div>
  <h2 class="abs">Hire a world-class gardening &amp; lawn care service in under two minutes.</h2>
  <p class="abs">Lorem ipsum dolor sit amet, consectetur adipiscing elit. Ut elit tellus, luctus nec ullamcorper mattis, pulvinar dapibus leo.</p>
  <div class="abs btn">Contact Us</div>
  <div class="abs play"><svg width="20" height="20" viewBox="0 0 20 20"><path d="M6 3l11 7-11 7z" fill="#fff"/></svg></div>
</section>

<footer class="abs footer">
  <div class="abs rule"></div>
  <div class="abs copy">Copyright &copy; 2021 Oakline. All rights reserved. Present by Birchway Studio.</div>
  <div class="abs legal"><span>Privacy Policy</span><span>Cookie Policy</span></div>
</footer>
<div class="abs footer-card">
  <div class="brandline"><span class="mark"></span>Oakline</div>
  <p>Lorem ipsum dolor sit amet, consectetur adipiscing elit. Ut elit tellus, luctus nec ullamcorper mattis, pulvinar dapibus leo.</p>
  <div class="socials"><span class="dot"></span><span class="dot"></span><span class="dot"></span></div>
</div>
<div class="abs fcol" style="left:526px;color:#fff"><h4>About</h4><ul><li>Home</li><li>About</li><li>Services</li><li>Gallery</li></ul></div>
<div class="abs fcol" style="left:735px;color:#fff"><h4>Support</h4><ul><li>Home</li><li>About</li><li>Services</li><li>Gallery</li></ul></div>
<div class="abs fcol" style="left:946px;width:160px;color:#fff"><h4>Office</h4>
  <div class="office-item"><i></i><div><b>Headquarter</b>42 Maple Row, Riverton</div></div>
  <div class="office-item"><i></i><div><b>Email Us</b>hello@oakline.example</div></div>
  <div class="office-item"><i></i><div><b>Call Us</b>+1 555 014 8220</div></div>
</div>

</body>
</html>
```